New skin and beauty clinic opening in Western Australia

The clinic is called Coral Hollow Skin & Beauty Clinic. We need a logo including a Palm tree and beach scene.
We are working out of an existing medical centre with large treatment room and new private rooms for out of hours consultations.
Treatments plans will be made with the (doctor) resident aesthetic physician 1st. With the doctor and two highly trained nurses all providing a vast range of treatments.
We have just purchased brand new state of the art technologically advanced machines.
We have lots of images and posters of the IPL& laser machines purchased that I would like to include on the site. We will also stock cosmeceuticals only available to registered doctors to be sold from the clinic. I will likely have lots of images from these to add to the site.
Prices will be determined after an initial consult with the Dr. This small fee will be taken off the final bill.
Free essential skin cancer checks with each
new patient!
The list treatments we will be offering are as
listed.
IPL permanent hair reduction (all hair colours)
IPL facial rejuvenation
IPL vascular treatments ( thread veins/rosacea)
IPL acne treatments
Fat cavitation for body sculpting /cellulite & weight loss
Weight loss clinic
Non surgical face/ neck & breast lifts
Laser Tattoo removal (many colours)
Tixaroll skin needling for resurfacing/ wrinkles/ scars & pigments& mesotherapy
Anti-wrinkle injections
Fillers
Microdermabrasion state of the art wet and dry with optional mini peel
Medical peels wide range

Also usual range of minor Beauty treatments
Facials, eyebrow waxing, tinting, bridal and formal make-up, acrylic and gel nails, massage, manicures pedicures.

I would like to add PRP (platelet rich plasma) to our list of treatments thanks

I would like to have a link to our Facebook page , and some YouTube videos.

new patient!
listed.
IPL facial rejuvenation
IPL acne treatments
Weight loss clinic
Anti-wrinkle injections
Fillers
Medical peels wide range

Target Market(s)

Patients and clients looking for skin beauty and cosmetic treatments
Women and men young and old

Industry/Entity Type

Clinic

Number of Pages Required

1 page

Font styles to use
Script

Requirements
Must have
• Links to Images of our treatments
• Palm tree / beach background /logo
• Space for A list of our treatments and links to images/ explanations of treatments
• I have got the rights to use these marketing images. Please change any phone number on the images to our number and any address as our address as listed here. Also please change lumen glow to Coral Hollow logo.
• Coral Hollow Skin & Beauty Clinic
• 17 Kestrelmoor Avenue
• Warnbro
• 6169
• Western Australia
• Phone = (08) 94618452
• Mob= 0439527164
• Please include key words for our location Perth, Rockingham, Warnbro, Secret Harbour, Baldivis, Mandurah, Port Kennedy, Waikiki, Safety Bay, Singleton, Golden Bay, Madora Bay, Meadow Springs
Nice to have
• An image/ photo of staff near the top( uniforms haven't arrived in post yet)
• Some script font and sans serif
• I have added 31 mages please let me know if they have not loaded
• Please try to use some of the bright colours from the photos
• Dermavista Wellness clinic .com.au has a good list of procedures.

```html
<!DOCTYPE html>
<html lang="en">
<head>
<meta charset="utf-8">
<title>Coral Hollow Skin &amp; Beauty Clinic</title>
<link rel="stylesheet" href="https://fonts.googleapis.com/css2?family=Open+Sans:wght@400;600;700&family=Parisienne&display=swap">
<style>
:root{
  --blue:#2b78c2;
  --blue-deep:#1f5fa8;
  --teal:#1d8a8a;
  --green:#3aa87c;
  --sky:#7bb4e0;
  --footer:#2a6fb5;
  --footer-dark:#1f5a9a;
  --white:#ffffff;
  --ink:#1b1b1b;
  --grey:#8a8f96;
}
*{box-sizing:border-box;margin:0;padding:0}
html,body{width:1200px;height:3442px;overflow:hidden;background:var(--white)}
body{font-family:"Open Sans",Arial,sans-serif;color:var(--ink);position:relative}
.abs{position:absolute}

/* header */
.site-header{position:absolute;left:0;top:0;width:1200px;height:138px;background:var(--white)}
.brand{position:absolute;left:80px;top:16px;display:flex;align-items:center;gap:12px}
.brand-mark{width:76px;height:76px;border-radius:50%;border:3px solid var(--teal)}
.brand-name{font-weight:600;color:var(--teal);line-height:1.1}
.brand-name .line1{font-size:30px;display:block}
.brand-name .line2{font-size:18px;display:block}
.social{position:absolute;top:40px;right:55px;display:flex;gap:10px}
.social span{width:34px;height:34px;border-radius:50%;background:var(--green)}
.main-nav{position:absolute;top:106px;right:52px;display:flex;gap:40px;font-size:17px;color:var(--blue-deep);font-weight:600}

/* hero */
.hero{position:absolute;left:0;top:138px;width:1200px;height:488px;
  background:linear-gradient(100deg,#c9c5c2 0%,#e9e5e1 30%,#d8cfc7 60%,#b9aea6 100%)}
.hero-title{position:absolute;left:103px;top:126px;font-size:40px;line-height:52px;color:var(--blue);font-weight:600;letter-spacing:.5px}
.hero-rule{position:absolute;left:103px;top:232px;width:585px;height:4px;background:var(--white)}

/* team */
.team-title{position:absolute;top:685px;width:1200px;text-align:center;font-size:30px;color:var(--teal);font-weight:600}
.team-sub{position:absolute;top:734px;width:1200px;text-align:center;font-size:17px;color:var(--blue)}
.member{position:absolute;top:802px;width:225px;height:350px;background:var(--white);
  box-shadow:0 0 6px rgba(0,0,0,.35);text-align:center}
.member .portrait{width:170px;height:170px;border-radius:50%;border:6px solid var(--blue);
  margin:14px auto 0;background:linear-gradient(160deg,#caa58e,#6d5246)}
.member .name{margin-top:30px;font-size:18px;font-weight:600;color:var(--blue-deep)}
.member .role{font-size:17px;color:var(--sky);margin-top:4px}
.member .links{display:flex;justify-content:center;gap:26px;margin-top:24px}
.member .links span{width:32px;height:32px;background:var(--green);border:2px solid #cfe9dd}

/* procedures */
.procedures{position:absolute;left:0;top:1223px;width:1200px;height:447px;
  background:linear-gradient(100deg,#1b5f93 0%,#2b82b8 45%,#5ea5cf 70%,#2478ad 100%)}
.proc-col{position:absolute;top:24px;width:380px;color:var(--white)}
.proc-col h3{font-size:21px;font-weight:400;margin-bottom:8px}
.proc-col li{list-style:none;border:1.5px solid rgba(255,255,255,.85);height:32px;line-height:29px;
  padding-left:6px;font-size:15px;margin-bottom:2.4px}

/* radio frequency */
.rf{position:absolute;left:0;top:1670px;width:1200px;height:636px;
  background:linear-gradient(90deg,#35dbe3 0%,#63e6ec 45%,#c7f5f8 100%)}
.rf-title{position:absolute;top:14px;left:400px;width:400px;text-align:center;font-size:28px;color:#1a5f8f;font-weight:600}
.rf-sub{position:absolute;top:52px;left:400px;width:400px;text-align:center;font-size:19px;color:#1a5f8f}
.expect{position:absolute;left:133px;top:82px;width:355px;height:470px;background:#050505;color:var(--white);padding:22px 24px}
.expect h3{font-size:21px;font-weight:700;margin-bottom:22px}
.expect h4{font-size:16px;font-weight:700}
.expect p{font-size:14px;line-height:20px;margin-bottom:22px;color:#e8e8e8}
.rf-photo{position:absolute;left:540px;top:80px;width:600px;height:556px;
  background:radial-gradient(ellipse at 60% 45%,#e8c4a8 0%,#c58d6a 40%,rgba(140,80,50,0) 75%)}

/* skin check banner */
.skin-check{position:absolute;left:0;top:2306px;width:1200px;height:316px;
  background:linear-gradient(100deg,#5a7ea8 0%,#9fb7d3 40%,#6f8fb8 70%,#4f6f9c 100%)}
.skin-check h2{position:absolute;right:57px;top:78px;text-align:right;color:var(--white);font-size:35px;line-height:52px;font-weight:700}
.btn-outline{position:absolute;top:196px;height:34px;border:2px solid var(--white);color:var(--white);
  font-size:17px;text-align:center;line-height:30px}

/* results */
.results{position:absolute;left:0;top:2622px;width:1200px;height:452px;background:var(--white)}
.figure-photo{position:absolute;left:0;top:0;width:370px;height:452px;
  background:linear-gradient(180deg,#d9b39c 0%,#efd6c6 50%,#f6f0ec 100%)}
.tagline{position:absolute;left:383px;top:140px;font-family:"Parisienne",cursive;font-size:26px;line-height:30px;color:var(--blue)}
.tag-rule{position:absolute;left:383px;top:208px;width:220px;height:1px;background:var(--sky)}
.tag-copy{position:absolute;left:383px;top:220px;width:320px;font-size:13px;line-height:20px;color:var(--blue)}
.results-title{position:absolute;left:730px;top:32px;font-size:24px;color:var(--blue)}
.shot{position:absolute;top:82px;width:172px;height:190px;background:linear-gradient(150deg,#e2a394,#b9675a)}
.shot span{position:absolute;left:6px;top:2px;font-size:16px;font-weight:700;color:var(--white)}
.results-note{position:absolute;left:730px;top:294px;width:410px;font-size:12.5px;line-height:18px;color:var(--grey)}
.btn-solid{position:absolute;left:727px;top:380px;width:140px;height:38px;background:var(--blue-deep);color:var(--white);
  font-size:14px;line-height:38px;text-align:center;font-weight:600}

/* footer */
.site-footer{position:absolute;left:0;top:3074px;width:1200px;height:321px;background:var(--footer);color:var(--white)}
.footer-brand{position:absolute;left:88px;top:58px;display:flex;align-items:center;gap:12px}
.footer-brand .brand-mark{border-color:var(--white)}
.footer-brand .brand-name{color:var(--white)}
.footer-about{position:absolute;left:88px;top:150px;width:310px;font-size:15px;line-height:23px}
.footer-head{position:absolute;top:62px;font-size:19px;font-weight:600}
.loc-list{position:absolute;top:108px;list-style:none;font-size:14px;line-height:30px}
.contact-list{position:absolute;left:935px;top:108px;list-style:none;font-size:15px;line-height:22px}
.contact-list li{display:flex;gap:10px;margin-bottom:4px}
.contact-list svg{flex:none;margin-top:4px}
.legal{position:absolute;left:0;top:3395px;width:1200px;height:47px;background:var(--footer-dark);
  color:var(--white);font-size:13px;text-align:center;line-height:47px}
</style>
</head>
<body>

<header class="site-header">
  <div class="brand">
    <span class="brand-mark"></span>
    <span class="brand-name"><span class="line1">Coral Hollow</span><span class="line2">Skin &amp; Beauty Clinic</span></span>
  </div>
  <div class="social"><span></span><span></span><span></span><span></span></div>
  <nav class="main-nav"><span>HOME</span><span>ABOUT</span><span>LASER TREATMENTS</span><span>SKIN TREATMENTS</span><span>CONTACT</span></nav>
</header>

<section class="hero" role="img" aria-label="Close-up photo of a woman receiving a microdermabrasion treatment">
  <h1 class="hero-title">EXPERIENCE THE FUTURE IN<br>MICRODERMABRASION</h1>
  <div class="hero-rule"></div>
</section>

<h2 class="team-title">OUR CREATIVE TEAM</h2>
<p class="team-sub">We are working out of the existing Coral Hollow Medical Centre with a large fully equipped treatment room</p>

<article class="member" style="left:165px">
  <div class="portrait" role="img" aria-label="Portrait photo of Elena"></div>
  <div class="name">ELENA</div><div class="role">Developer</div>
  <div class="links"><span></span><span></span><span></span></div>
</article>
<article class="member" style="left:491px">
  <div class="portrait" role="img" aria-label="Portrait photo of Tobias"></div>
  <div class="name">TOBIAS</div><div class="role">CEO</div>
  <div class="links"><span></span><span></span><span></span></div>
</article>
<article class="member" style="left:818px">
  <div class="portrait" role="img" aria-label="Portrait photo of Harold"></div>
  <div class="name">HAROLD</div><div class="role">President &amp; Founder</div>
  <div class="links"><span></span><span></span><span></span></div>
</article>

<section class="procedures" role="img" aria-label="Photo of a woman relaxing by a blue pool">
  <div class="proc-col" style="left:137px">
    <h3>Procedures We Provide</h3>
    <ul>
      <li>IPL permanent hair reduction (all hair colours)</li>
      <li>IPL facial rejuvenation</li>
      <li>IPL vascular treatments ( thread veins/rosacea)</li>
      <li>IPL acne treatments</li>
      <li>Weight loss clinic</li>
      <li>Non surgical face/ neck &amp; breast lifts</li>
      <li>Laser Tattoo removal (many colours)</li>
      <li>Anti-wrinkle injections</li>
      <li>Fillers</li>
      <li>Medical peels wide range</li>
    </ul>
  </div>
  <div class="proc-col" style="left:673px">
    <h3>Minor Beauty Treatments</h3>
    <ul>
      <li>Facials</li>
      <li>Eyebrow waxing</li>
      <li>Tinting</li>
      <li>Bridal and formal make-up</li>
      <li>Acrylic and gel nails</li>
      <li>Massage</li>
      <li>Manicures pedicures</li>
    </ul>
  </div>
</section>

<section class="rf">
  <h2 class="rf-title">RADIO FREQUENCY</h2>
  <p class="rf-sub">A difference you can see and feel</p>
  <div class="rf-photo" role="img" aria-label="Photo of a woman in profile touching her neck"></div>
  <div class="expect">
    <h3>What you can expect</h3>
    <h4>Tissue retraction</h4>
    <p>The heat causes local contraction of the collagen fibres, which immediately tightens the skin to reveal a lifted, tighter and more youthful appearance.</p>
    <h4>New collagen formation</h4>
    <p>Heating the dermis stimulates production of new collagen which is essential in the battle against signs of ageing. Increased collagen equals plumper, firmer skin with a greater level of elasticity.</p>
    <h4>Improved circulation</h4>
    <p>RF also improves the blood and lymphatic flow. This helps induce a better oxygen supply and greater toxin clearance to further reduce the signs and effects of ageing.</p>
  </div>
</section>

<section class="skin-check" role="img" aria-label="Soft blue-toned photo of a woman with flowing hair">
  <h2>FREE ESSENTIAL SKIN CANCER<br>CHECKS WITH EACH NEW PATIENT!</h2>
  <span class="btn-outline" style="left:733px;width:180px">Find out more</span>
  <span class="btn-outline" style="left:946px;width:180px">Book now</span>
</section>

<section class="results">
  <div class="figure-photo" role="img" aria-label="Photo of a slim waist with a measuring tape"></div>
  <p class="tagline">Sculpt your figure<br>Enhance your silhouette</p>
  <div class="tag-rule"></div>
  <p class="tag-copy">The combination of Fractional RF and Dermal Stamping involves direct energy into the layers of the skin. This micro-needle treatment will stimulate the production of collagen and elastin.</p>
  <h3 class="results-title">Amazing results</h3>
  <div class="shot" style="left:730px" role="img" aria-label="Close-up photo of skin before treatment"><span>Before</span></div>
  <div class="shot" style="left:957px" role="img" aria-label="Close-up photo of skin after treatment"><span>After</span></div>
  <p class="results-note">This is sample placeholder text. Proin gravida nibh vel velit auctor aliquet. Aenean sollicitudin, lorem quis bibendum auctor, nisi elit consequat ipsum, nec sagittis sem nibh id elit.</p>
  <span class="btn-solid">MORE RESULTS &#9656;</span>
</section>

<footer class="site-footer">
  <div class="footer-brand">
    <span class="brand-mark"></span>
    <span class="brand-name"><span class="line1">Coral Hollow</span><span class="line2">Skin &amp; Beauty Clinic</span></span>
  </div>
  <p class="footer-about">We are working out of the existing Coral Hollow Medical Centre with a large fully equipped treatment room and a brand new private consultation room in Secret Harbour for out of hours consultations.</p>

  <h4 class="footer-head" style="left:440px">CLINIC LOCATIONS</h4>
  <ul class="loc-list" style="left:440px">
    <li>Beauty Clinic in Perth</li><li>Beauty Clinic in Rockingham</li><li>Beauty Clinic in Warnbro</li>
    <li>Beauty Clinic in Secret Harbour</li><li>Beauty Clinic in Baldivis</li><li>Beauty Clinic in Mandurah</li>
    <li>Beauty Clinic in Port Kennedy</li>
  </ul>
  <ul class="loc-list" style="left:688px">
    <li>Beauty Clinic in Waikiki</li><li>Beauty Clinic in Safety Bay</li><li>Beauty Clinic in Singleton</li>
    <li>Beauty Clinic in Golden Bay</li><li>Beauty Clinic in Madora Bay</li><li>Beauty Clinic in Meadow Springs</li>
  </ul>

  <h4 class="footer-head" style="left:935px">CONTACT</h4>
  <ul class="contact-list">
    <li><svg width="12" height="16" viewBox="0 0 12 16"><path d="M6 0a6 6 0 0 0-6 6c0 4.5 6 10 6 10s6-5.5 6-10a6 6 0 0 0-6-6zm0 8.5A2.5 2.5 0 1 1 6 3.5a2.5 2.5 0 0 1 0 5z" fill="#7fe0b8"/></svg>
      <span>17 Kestrelmoor Avenue,<br>Warnbro 6169,<br>Western Australia</span></li>
    <li><svg width="14" height="11" viewBox="0 0 14 11"><rect width="14" height="11" rx="1" fill="#7fe0b8"/><path d="M0 1l7 5 7-5" stroke="#2a6fb5" stroke-width="1.4" fill="none"/></svg>
      <span>info@coralhollowclinic.com.au</span></li>
    <li style="margin-top:14px"><svg width="13" height="13" viewBox="0 0 13 13"><path d="M3 0l2 3-1.3 1.6a8 8 0 0 0 4.7 4.7L10 8l3 2-1.5 2.5C6 12.5.5 7 .5 1.5z" fill="#7fe0b8"/></svg>
      <span>(08) 9461 8452</span></li>
  </ul>
</footer>
<div class="legal">© 2015 Coral Hollow Skin &amp; Beauty Clinic| All rights reserved.</div>

</body>
</html>
```